Social Media Graphics - Copperfield Loop

Create 6-7 individual social media graphics (square size) to encourage folks to join our online course, using either of the text below (only one set of text per graphic:

The Lantern Ridge Method
How to Create a 7-Figure Business From Scratch
Sign Up Today!

Or

The Lantern Ridge Method
Fast-track Your Way to a Multi-Million Business!
Sign Up Today!

For the color scheme of the graphics, use 1 or 2 colors in the color palette attached; or use any colors that look nice with their outfits; AVOID using red, white and blue altogether because it will look like an Independence Day (4th of July) graphic and we don’t want that; make sure the graphics appeal to both men and women

Make sure each graphic contains 1 of the 2 pics attached; and make sure one of the graphics is all TEXT only.

Target Market(s)

men and women looking to make more money

Industry/Entity Type

entrepreneurship

Requirements
Must have
• see the text document attached
Nice to have
• We are open to a nice color design; the color palette colors are not required, especially we don't want red, white and blue used together
Should not have
• AVOID using red, white and blue altogether because it will look like an Independence Day (4th of July) graphic and we dont want that

```html
<!DOCTYPE html>
<html lang="en">
<head>
<meta charset="utf-8">
<title>The Lantern Ridge Method – Social Graphic</title>
<link rel="stylesheet" href="https://fonts.googleapis.com/css2?family=Righteous&family=Montserrat+Alternates:wght@500;600;800&family=Montserrat:wght@800&display=swap">
<style>
  :root {
    --page-bg: #f8c4d3;
    --purple-deep: #3a1d7a;
    --purple-mid: #6a2a96;
    --magenta: #a2347f;
    --indigo: #2b2690;
    --panel-pink: #f1a3e6;
    --panel-lilac: #c3a5ee;
    --panel-blue: #6fb4ef;
    --ink-navy: #1c1a55;
    --ink-blue: #1d1fc6;
    --cta: #ec3469;
    --white: #ffffff;
  }
  * { box-sizing: border-box; margin: 0; padding: 0; }
  html, body {
    width: 1200px; height: 969px; overflow: hidden;
    background: var(--page-bg);
  }
  .ad {
    position: absolute; left: 150px; top: 34px;
    width: 900px; height: 900px; overflow: hidden;
    background: radial-gradient(ellipse at 30% 0%, var(--magenta) 0%, transparent 55%),
                linear-gradient(160deg, var(--purple-mid) 0%, #4f2590 55%, var(--indigo) 100%);
  }
  .ad__eyebrow {
    position: absolute; left: 74px; top: 58px;
    font-family: "Righteous", sans-serif;
    font-size: 58px; color: var(--white); letter-spacing: 1px;
  }
  .ad__title {
    position: absolute; left: 70px; top: 118px;
    font-family: "Righteous", sans-serif;
    font-size: 128px; line-height: 1; color: var(--white);
    letter-spacing: 4px;
    text-shadow: 4px 4px 0 var(--purple-deep);
  }
  .ad__panel {
    position: absolute; left: 0; top: 285px;
    width: 832px; height: 407px;
    border-top-right-radius: 56px;
    background: linear-gradient(100deg, var(--panel-pink) 0%, var(--panel-lilac) 45%, var(--panel-blue) 100%);
  }
  .ad__glow {
    position: absolute; left: 0; height: 3px; width: 832px;
    background: linear-gradient(90deg, transparent, #ffd6ff 40%, transparent);
  }
  .ad__glow--top { top: 284px; }
  .ad__glow--bottom { top: 691px; }
  .ad__headline {
    position: absolute; left: 74px; top: 318px;
    font-family: "Montserrat Alternates", sans-serif;
    font-weight: 500; font-size: 54px; line-height: 67px;
    color: var(--ink-navy);
  }
  .ad__headline strong { font-weight: 800; color: var(--ink-blue); }
  .ad__photo {
    position: absolute; left: 500px; top: 386px;
    width: 400px; height: 514px;
    border-radius: 200px 200px 0 0;
    background: linear-gradient(180deg, #2d2340 0%, #c8355e 55%, #23202e 100%);
    opacity: 0.92;
  }
  .ad__cta {
    position: absolute; left: 50px; top: 757px;
    width: 303px; height: 83px; border-radius: 42px;
    background: var(--cta);
    display: flex; align-items: center; justify-content: center;
    font-family: "Montserrat", sans-serif; font-weight: 800;
    font-size: 34px; color: var(--white); letter-spacing: 1px;
  }
</style>
</head>
<body>
  <main class="ad">
    <p class="ad__eyebrow">THE LANTERN RIDGE</p>
    <h1 class="ad__title">METHOD</h1>
    <div class="ad__panel"></div>
    <div class="ad__glow ad__glow--top"></div>
    <div class="ad__glow ad__glow--bottom"></div>
    <h2 class="ad__headline">How to Create<br>a <strong>7-Figure</strong><br><strong>Business</strong><br>From<br>Scratch</h2>
    <div class="ad__photo" role="img" aria-label="Photo of the two course hosts, a woman in a pink dress and a man in black, smiling with arms crossed"></div>
    <a class="ad__cta">JOIN NOW!</a>
  </main>
</body>
</html>
```